Saveurs Du Matin LLC New Chirpbook Page

Hello we would like to have a nice banner display of our products it should be innovated but very inviting we want to grow our base and reach new clients. each product should be highlighted with an overall great appearance. maybe use of salts in the background.

our logo is on our page, please use that logo.

***Please visit our page and look at albums all of our products are there, the files are too big to upload.

https://www.example-social.com/saveursdumatin/?fref=ts&ref=br_tf

Cheers

Target Market(s)

foodies, cooks, chefs, gourmet, boutique

Industry/Entity Type

Food Store

Font styles to use
Script

Colors
ffffff
fce8d3
f59195
33a6d7

Requirements
Must have
• clean and clear understanding of who we are, must be able to easily hand over so we can make adjustments of our own.
Nice to have
• link to coinpost
Should not have
• cartoon characters or style

```html
<!DOCTYPE html>
<html lang="en">
<head>
<meta charset="utf-8">
<title>Saveurs Du Matin – Chirpbook Page Banner</title>
<link href="https://fonts.googleapis.com/css2?family=Great+Vibes&family=Open+Sans:wght@400;600;700&family=Roboto:wght@300&family=Teko:wght@500&display=swap" rel="stylesheet">
<style>
  :root {
    --board: #262626;
    --board-label: #b9b9b9;
    --brown: #5b3318;
    --brown-deep: #4a2811;
    --gold: #d8ad63;
    --gold-light: #e7c486;
    --gold-dark: #b88a43;
    --dot: #a0663a;
    --cream: #fff9f0;
    --sand-edge: #f0d9ae;
    --peach-edge: #f6c6a3;
    --white: #ffffff;
  }
  * { margin: 0; padding: 0; box-sizing: border-box; }
  html, body { width: 1200px; height: 1200px; overflow: hidden; }
  body { background: var(--board); position: relative; font-family: "Open Sans", sans-serif; }

  .sample-title {
    position: absolute; left: 0; width: 1200px; text-align: center;
    font-family: "Open Sans", sans-serif; font-weight: 400; font-size: 32px;
    color: var(--board-label); line-height: 1;
  }
  .sample-title--one { top: 24px; }
  .sample-title--two { top: 620px; }

  .banner { position: absolute; left: 142px; width: 916px; height: 478px; display: block; }
  .banner--sand { top: 82px; }
  .banner--peach { top: 672px; }

  .ribbon-text { font-family: "Teko", sans-serif; font-size: 20px; fill: var(--white); letter-spacing: 0.5px; }
  .brand-name { font-family: "Great Vibes", cursive; font-size: 30px; fill: var(--brown); }
  .brand-tagline { font-family: "Great Vibes", cursive; font-size: 11px; fill: var(--brown); letter-spacing: 1.5px; }
  .product-label { font-family: "Open Sans", sans-serif; font-weight: 600; font-size: 11px; fill: var(--brown-deep); letter-spacing: 0.4px; }
  .like-text { font-family: "Roboto", sans-serif; font-weight: 300; font-size: 17px; fill: var(--white); }
  .phone-text { font-family: "Roboto", sans-serif; font-weight: 300; font-size: 18px; fill: var(--white); }
</style>
</head>
<body>

<h2 class="sample-title sample-title--one">Sample 1</h2>

<svg class="banner banner--sand" viewBox="0 0 916 478" aria-label="Saveurs Du Matin page banner, sand version">
  <defs>
    <radialGradient id="sand-bg" cx="50%" cy="45%" r="70%">
      <stop offset="0" stop-color="#ffffff"/>
      <stop offset="0.45" stop-color="#f8ecdb"/>
      <stop offset="1" stop-color="#ecd3a4"/>
    </radialGradient>
    <radialGradient id="peach-bg" cx="50%" cy="40%" r="70%">
      <stop offset="0" stop-color="#ffffff"/>
      <stop offset="0.45" stop-color="#fbe7d7"/>
      <stop offset="1" stop-color="#f5c19d"/>
    </radialGradient>
    <linearGradient id="band" x1="0" y1="0" x2="0" y2="1">
      <stop offset="0" stop-color="#e7c486"/>
      <stop offset="1" stop-color="#c99a52"/>
    </linearGradient>
    <linearGradient id="jar" x1="0" y1="0" x2="0" y2="1">
      <stop offset="0" stop-color="#cfcfcf"/>
      <stop offset="0.18" stop-color="#3e3a33"/>
      <stop offset="0.25" stop-color="#f1ece3"/>
      <stop offset="0.6" stop-color="#ece4d6"/>
      <stop offset="0.7" stop-color="#9a7a4c"/>
      <stop offset="1" stop-color="#b5956a"/>
    </linearGradient>
  </defs>

  <rect class="banner-bg" width="916" height="478" fill="url(#sand-bg)" role="img" aria-label="Fine sea salt texture background"/>

  <!-- official page ribbon -->
  <path d="M29 0 H94 V70 L61.5 82 L29 70 Z" fill="var(--brown)"/>
  <text class="ribbon-text" x="61.5" y="40" text-anchor="middle">OFFICIAL</text>
  <text class="ribbon-text" x="61.5" y="62" text-anchor="middle">PAGE</text>

  <!-- brand -->
  <circle cx="458" cy="66" r="40" fill="none" stroke="var(--dot)" stroke-width="2"/>
  <text class="brand-name" x="458" y="130" text-anchor="middle">Saveurs Du Matin</text>
  <text class="brand-tagline" x="458" y="146" text-anchor="middle">Highest Quality Spices</text>

  <!-- products -->
  <g class="product">
    <circle cx="164" cy="254" r="78" fill="none" stroke="var(--dot)" stroke-width="5" stroke-dasharray="0 15" stroke-linecap="round"/>
    <circle cx="164" cy="254" r="62" fill="var(--brown)"/>
    <rect x="134" y="156" width="60" height="150" rx="10" fill="url(#jar)" role="img" aria-label="Jar of fish seasoning"/>
    <rect x="88" y="235" width="152" height="21" rx="2" fill="url(#band)"/>
    <text class="product-label" x="164" y="250" text-anchor="middle">FISH SEASONING</text>
  </g>
  <g class="product">
    <circle cx="362" cy="254" r="78" fill="none" stroke="var(--dot)" stroke-width="5" stroke-dasharray="0 15" stroke-linecap="round"/>
    <circle cx="362" cy="254" r="62" fill="var(--brown)"/>
    <rect x="332" y="156" width="60" height="150" rx="10" fill="url(#jar)" role="img" aria-label="Jar of meat rub"/>
    <rect x="286" y="235" width="152" height="21" rx="2" fill="url(#band)"/>
    <text class="product-label" x="362" y="250" text-anchor="middle">MEAT RUB</text>
  </g>
  <g class="product">
    <circle cx="558" cy="254" r="78" fill="none" stroke="var(--dot)" stroke-width="5" stroke-dasharray="0 15" stroke-linecap="round"/>
    <circle cx="558" cy="254" r="62" fill="var(--brown)"/>
    <rect x="528" y="156" width="60" height="150" rx="10" fill="url(#jar)" role="img" aria-label="Jar of southwest rib rub"/>
    <rect x="482" y="235" width="152" height="21" rx="2" fill="url(#band)"/>
    <text class="product-label" x="558" y="250" text-anchor="middle">SOUTHWEST RIB RUB</text>
  </g>
  <g class="product">
    <circle cx="754" cy="254" r="78" fill="none" stroke="var(--dot)" stroke-width="5" stroke-dasharray="0 15" stroke-linecap="round"/>
    <circle cx="754" cy="254" r="62" fill="var(--brown)"/>
    <rect x="724" y="156" width="60" height="150" rx="10" fill="url(#jar)" role="img" aria-label="Jar of amazing veggies seasoning"/>
    <rect x="678" y="235" width="152" height="21" rx="2" fill="url(#band)"/>
    <text class="product-label" x="754" y="250" text-anchor="middle">AMAZING VEGGIES</text>
  </g>

  <!-- call to action -->
  <path d="M374 350 Q384 380 418 390 M406 383 L418 390 L406 396" fill="none" stroke="var(--gold)" stroke-width="2"/>
  <path d="M554 350 Q544 380 510 390 M522 383 L510 390 L522 396" fill="none" stroke="var(--gold)" stroke-width="2"/>
  <circle cx="464" cy="413" r="45" fill="var(--gold)"/>
  <text class="like-text" x="464" y="432" text-anchor="middle">Like Us!</text>

  <!-- footer bars -->
  <path d="M0 430 H250 L278 478 H0 Z" fill="var(--brown)"/>
  <g class="payment-badges">
    <rect x="13" y="440" width="37" height="26" rx="2" fill="#f2f2f2"/>
    <rect x="56" y="440" width="37" height="26" rx="2" fill="#3a9fd8"/>
    <rect x="101" y="440" width="37" height="26" rx="2" fill="#f2f2f2"/>
    <rect x="144" y="440" width="37" height="26" rx="2" fill="#f2f2f2"/>
    <rect x="189" y="440" width="37" height="26" rx="2" fill="#f2f2f2"/>
  </g>
  <path d="M916 430 H666 L640 478 H916 Z" fill="var(--brown)"/>
  <text class="phone-text" x="898" y="462" text-anchor="end">(042) 555 014 - 555 017 820</text>
</svg>

<h2 class="sample-title sample-title--two">Sample 2</h2>

<svg class="banner banner--peach" viewBox="0 0 916 478" aria-label="Saveurs Du Matin page banner, peach version">
  <rect class="banner-bg" width="916" height="478" fill="url(#peach-bg)" role="img" aria-label="Soft peach plaster texture background"/>

  <path d="M29 0 H94 V70 L61.5 82 L29 70 Z" fill="var(--brown)"/>
  <text class="ribbon-text" x="61.5" y="40" text-anchor="middle">OFFICIAL</text>
  <text class="ribbon-text" x="61.5" y="62" text-anchor="middle">PAGE</text>

  <circle cx="458" cy="66" r="40" fill="none" stroke="var(--dot)" stroke-width="2"/>
  <text class="brand-name" x="458" y="130" text-anchor="middle">Saveurs Du Matin</text>
  <text class="brand-tagline" x="458" y="146" text-anchor="middle">Highest Quality Spices</text>

  <g class="product">
    <circle cx="164" cy="254" r="78" fill="none" stroke="var(--dot)" stroke-width="5" stroke-dasharray="0 15" stroke-linecap="round"/>
    <circle cx="164" cy="254" r="62" fill="var(--brown)"/>
    <rect x="134" y="156" width="60" height="150" rx="10" fill="url(#jar)" role="img" aria-label="Jar of fish seasoning"/>
    <rect x="88" y="235" width="152" height="21" rx="2" fill="url(#band)"/>
    <text class="product-label" x="164" y="250" text-anchor="middle">FISH SEASONING</text>
  </g>
  <g class="product">
    <circle cx="362" cy="254" r="78" fill="none" stroke="var(--dot)" stroke-width="5" stroke-dasharray="0 15" stroke-linecap="round"/>
    <circle cx="362" cy="254" r="62" fill="var(--brown)"/>
    <rect x="332" y="156" width="60" height="150" rx="10" fill="url(#jar)" role="img" aria-label="Jar of meat rub"/>
    <rect x="286" y="235" width="152" height="21" rx="2" fill="url(#band)"/>
    <text class="product-label" x="362" y="250" text-anchor="middle">MEAT RUB</text>
  </g>
  <g class="product">
    <circle cx="558" cy="254" r="78" fill="none" stroke="var(--dot)" stroke-width="5" stroke-dasharray="0 15" stroke-linecap="round"/>
    <circle cx="558" cy="254" r="62" fill="var(--brown)"/>
    <rect x="528" y="156" width="60" height="150" rx="10" fill="url(#jar)" role="img" aria-label="Jar of southwest rib rub"/>
    <rect x="482" y="235" width="152" height="21" rx="2" fill="url(#band)"/>
    <text class="product-label" x="558" y="250" text-anchor="middle">SOUTHWEST RIB RUB</text>
  </g>
  <g class="product">
    <circle cx="754" cy="254" r="78" fill="none" stroke="var(--dot)" stroke-width="5" stroke-dasharray="0 15" stroke-linecap="round"/>
    <circle cx="754" cy="254" r="62" fill="var(--brown)"/>
    <rect x="724" y="156" width="60" height="150" rx="10" fill="url(#jar)" role="img" aria-label="Jar of amazing veggies seasoning"/>
    <rect x="678" y="235" width="152" height="21" rx="2" fill="url(#band)"/>
    <text class="product-label" x="754" y="250" text-anchor="middle">AMAZING VEGGIES</text>
  </g>

  <path d="M374 350 Q384 380 418 390 M406 383 L418 390 L406 396" fill="none" stroke="var(--gold)" stroke-width="2"/>
  <path d="M554 350 Q544 380 510 390 M522 383 L510 390 L522 396" fill="none" stroke="var(--gold)" stroke-width="2"/>
  <circle cx="464" cy="413" r="45" fill="var(--gold)"/>
  <text class="like-text" x="464" y="432" text-anchor="middle">Like Us!</text>

  <path d="M0 430 H250 L278 478 H0 Z" fill="var(--brown)"/>
  <g class="payment-badges">
    <rect x="13" y="440" width="37" height="26" rx="2" fill="#f2f2f2"/>
    <rect x="56" y="440" width="37" height="26" rx="2" fill="#3a9fd8"/>
    <rect x="101" y="440" width="37" height="26" rx="2" fill="#f2f2f2"/>
    <rect x="144" y="440" width="37" height="26" rx="2" fill="#f2f2f2"/>
    <rect x="189" y="440" width="37" height="26" rx="2" fill="#f2f2f2"/>
  </g>
  <path d="M916 430 H666 L640 478 H916 Z" fill="var(--brown)"/>
  <text class="phone-text" x="898" y="462" text-anchor="end">(042) 555 014 - 555 017 820</text>
</svg>

</body>
</html>
```